Brisk Mist Premium Cooling Towel

Similar to Tan Goat, Vantrel and Pebble. Brisk Mist's Products are a premium brand within the cooling market. From towels to high performance sports products Brisk Mists products crush the competitors. The product regardless of the conditions stays cold even in the hottest conditions. Our current clients range from the Grand Lanterns, Hollis Merrow's to professional athletes. We are currently redesigning our packaging for our towel line.

The goal of this design is to have someone look at the package and say "Whoa...". When customers first try the product they have a good idea of what to expect, then they try it and are blown away. Simply put the towel sells itself. Sales reps have stated that the highest closing rates are when they say nothing at all.

With that being said we are looking for a packaging that has the same effect. Imagine you are sitting by the pool side in Miami in the middle of the summer, you feel like your body is on fire. Someone then offers you a brisk mist towel that instantly cools you making the unbearable suddenly... enjoyable.

Yes, this is the effect we are looking for off the shelf. If this were on the shelf at Shopvale in the container how do we get this same effect. Things that our customers have indicated were a plus was when the cooling effect was displayed by both color and transition of the logo. This effect typically takes some layering in photo shop but when done right results in a much higher customer rating.

The containers are a plastic tube (roughly 10 inch by 3 inch in by diameter) and an envelope style pouch that is 10inch by 6inch. Official dimensions will be updated later this week.

We are looking for a simple clean look that screams "premium". Again, the "whoa" factor is a must to stand out against competitors. The main color schemes to consider are hot red, Ice cold blue, silver, black. Realizing that building a a compelling design that relates to an audience of 16-30 Male and Female is tough please ask questions. It must connect to parents, teens and active athletes. Again, think Tan Goat and how it connects with everyone.

Competitors:
1. http://www.buildkitdepot.example/brix-lane-breezy-sport-cooling-towel.html?id=10293847560

2.http://www.valuebarnoutlet.example/product/3-4418290?ref=shop

3. http://www.marketrivo.example/Quest-Steadyfrost-Instant-Cooling-Towel/dp/Q7TR2LMX40/ref=sim_2

4. http://www.frostwrapz.example/

5. http://www.halvorwear.example/Tera-Glaze-Cooling-Performance-Clothing-Apparel/Technology_Tera-Glaze_Nil,default,pg.html

6. http://www.searchloom.example/shopping/pine-ridge-outfitters-harbor-hawks-cooling-towel-white-5503811/p/C7DA19F0A3B2?q=cooling+towel

7. http://www.marigoldmailer.example/p/Polar-Nip-Towel-Blue.cfm?tid=338104522

8.https://www.breezecloths.example/

9. http://www.pricedrift.example/cooling-towels/products-html#!

Reason: Due to a massive influx of designs we will be extending the project for four additional days to fairly evaluate all of the designs. No new designs will be considered after today (April 19th). I will be sending out the designs to our network and the one that gets the most votes wins. I really appreciate all of the different designs and will keep you posted on the vote count.

Target Market(s)

16-30, Male, Female, Moms, Dad's and active athletes of all ages

Industry/Entity Type

Clothing

Requirements
Must have
• Simply put I want people to say "whoa..."". When they use the product they say it and instantly buy almost every time. Unfortunately i can't have everyone get to have a free demo. So I need the packaging to convey this and make people feel like it's the party they want to be invited to
Nice to have
• Think Tan Goat and Pebble. Relates to a very wide ranging diverse audience
Should not have
• Not to look stupid, Cartoony or childish. This is not a gimick, it is a great product at a fair price. People have no problem paying for something that works and the packaging needs to reflect the same

```html
<!DOCTYPE html>
<html lang="en">
<head>
<meta charset="utf-8">
<title>Brisk Mist Cooling Towel – Tube Wraps</title>
<link rel="stylesheet" href="https://fonts.googleapis.com/css2?family=Open+Sans:wght@400;700&display=swap">
<style>
  :root {
    --bg: #e3e7ed;
    --ice-blue: #1b8ad6;
    --deep-blue: #0f5fb8;
    --hot-red: #e5282a;
    --silver-light: #f4f6f8;
    --silver-mid: #d6dbe2;
    --silver-dark: #a9adbd;
    --white: #ffffff;
  }
  * { margin: 0; padding: 0; box-sizing: border-box; }
  html, body { width: 1200px; height: 849px; overflow: hidden; }
  body {
    background: var(--bg);
    font-family: "Open Sans", Arial, sans-serif;
    position: relative;
  }
  .wrap {
    position: absolute;
    top: 73px;
    width: 193px;
    height: 663px;
  }
  .wrap--classic { left: 135px; }
  .wrap--wave { left: 452px; }
  .wrap--dots { left: 764px; }
  .wrap svg { display: block; }
  .brand-name { font-family: "Open Sans", Arial, sans-serif; font-weight: 700; fill: var(--ice-blue); }
  .copy { font-family: "Open Sans", Arial, sans-serif; font-weight: 400; fill: var(--ice-blue); }
  .copy--red { fill: var(--hot-red); }
  .copy--white { fill: var(--white); }
</style>
</head>
<body>

<svg width="0" height="0" aria-hidden="true" style="position:absolute">
  <defs>
    <linearGradient id="silver" x1="0" y1="0" x2="1" y2="0">
      <stop offset="0" stop-color="#c8ced6"/>
      <stop offset="0.35" stop-color="#f4f6f8"/>
      <stop offset="0.7" stop-color="#d9dde4"/>
      <stop offset="1" stop-color="#9c9fb3"/>
    </linearGradient>
    <linearGradient id="band" x1="0" y1="0" x2="1" y2="0">
      <stop offset="0" stop-color="#1b7fd4"/>
      <stop offset="1" stop-color="#0d47a8"/>
    </linearGradient>
    <linearGradient id="accent-fill" x1="0" y1="0" x2="0" y2="1">
      <stop offset="0" stop-color="#1b8ad6" stop-opacity="0.22"/>
      <stop offset="1" stop-color="#1b8ad6" stop-opacity="0.08"/>
    </linearGradient>
  </defs>
</svg>

<!-- Wrap 1: classic vertical -->
<div class="wrap wrap--classic">
  <svg width="193" height="663" viewBox="0 0 193 663">
    <rect class="wrap-surface" width="193" height="663" fill="url(#silver)"/>
    <circle cx="52" cy="224" r="18" fill="var(--hot-red)"/>
    <text class="brand-name" font-size="38" text-anchor="middle" transform="translate(138 224) rotate(-90)">Brisk Mist</text>
    <g class="copy" font-size="15" transform="rotate(-90)">
      <text x="-605" y="83">Instant COOLING TOWEL</text>
      <text x="-605" y="104">simple wet and shake to</text>
      <text x="-580" y="125">stay cool for huot's</text>
    </g>
    <rect class="base-band" y="622" width="193" height="41" fill="url(#band)"/>
    <line x1="0" y1="622" x2="193" y2="622" stroke="var(--hot-red)" stroke-width="2"/>
    <text class="copy copy--white" x="96" y="650" font-size="15" text-anchor="middle">washable and reusable</text>
  </svg>
</div>

<!-- Wrap 2: blue wave with activity icons -->
<div class="wrap wrap--wave">
  <svg width="193" height="663" viewBox="0 0 193 663">
    <rect class="wrap-surface" width="193" height="663" fill="url(#silver)"/>
    <path class="top-wave" d="M0 0 H193 V69 C110 85 40 140 0 215 Z" fill="url(#band)"/>
    <path d="M193 69 C110 85 40 140 0 215" fill="none" stroke="var(--hot-red)" stroke-width="2"/>
    <circle cx="56" cy="256" r="16" fill="var(--hot-red)"/>
    <text class="brand-name" font-size="32" text-anchor="middle" transform="translate(140 260) rotate(-90)">Brisk Mist</text>
    <g class="activity-icons">
      <rect x="36" y="419" width="36" height="36" rx="6" fill="var(--ice-blue)" role="img" aria-label="Cycling pictogram"/>
      <rect x="36" y="462" width="36" height="36" rx="6" fill="var(--ice-blue)" role="img" aria-label="Running pictogram"/>
      <rect x="36" y="505" width="36" height="36" rx="6" fill="var(--ice-blue)" role="img" aria-label="Swimming pictogram"/>
      <rect x="36" y="548" width="36" height="36" rx="6" fill="var(--ice-blue)" role="img" aria-label="Stretching pictogram"/>
    </g>
    <g class="copy" font-size="15" transform="rotate(-90)">
      <text x="-600" y="96">Instant COOLING TOWEL</text>
      <text x="-600" y="117">simple wet and shake to</text>
      <text x="-575" y="138">stay cool for huot's</text>
      <text class="copy--red" x="-585" y="159">washable and reusable</text>
    </g>
    <rect class="base-band" y="624" width="193" height="39" fill="url(#band)"/>
    <line x1="0" y1="624" x2="193" y2="624" stroke="var(--hot-red)" stroke-width="2"/>
  </svg>
</div>

<!-- Wrap 3: centered layout with decorative panels -->
<div class="wrap wrap--dots">
  <svg width="193" height="663" viewBox="0 0 193 663">
    <rect class="wrap-surface" width="193" height="663" fill="url(#silver)"/>
    <rect class="decor-panel decor-panel--top" x="25" y="80" width="143" height="96" rx="8" fill="url(#accent-fill)" role="img" aria-label="Blue dotted chevron pattern pointing up"/>
    <circle cx="97" cy="244" r="17" fill="var(--hot-red)"/>
    <text class="brand-name" x="97" y="297" font-size="30" text-anchor="middle">Brisk Mist</text>
    <text class="copy" x="97" y="391" font-size="13" text-anchor="middle">INSTANT COOLING TOWEL</text>
    <text class="copy" x="97" y="424" font-size="13" text-anchor="middle">simple wet and shake to</text>
    <text class="copy" x="97" y="441" font-size="13" text-anchor="middle">stay cool for huot's</text>
    <rect class="decor-panel decor-panel--bottom" x="25" y="520" width="143" height="96" rx="8" fill="url(#accent-fill)" role="img" aria-label="Blue dotted chevron pattern pointing down"/>
    <text class="copy" x="97" y="650" font-size="15" text-anchor="middle">washable and reusable</text>
  </svg>
</div>

</body>
</html>
```